Business Card for Lorena Whitfield

Name: Lorena Whitfield
Title: Realtor
Email: Lorena@LorenaWhitfieldRE.com
Phone: 480-555-0137

On the front of the business card, I would like the photo, the contact information and the Lorena Whitfield Logo. The backside is required to have the Broker logo and the required logos. Please use the colors from the logo design. Our company has a classy, professional look.

```html
<!DOCTYPE html>
<html lang="en">
<head>
<meta charset="utf-8">
<title>Lorena Whitfield Real Estate – Business Card</title>
<link rel="stylesheet" href="https://fonts.googleapis.com/css2?family=Cinzel:wght@400;600&family=Arimo:wght@400&display=swap">
<style>
  :root {
    --crimson: #b80c37;
    --charcoal: #4a4a4a;
    --ink: #2b2b2b;
    --paper: #ffffff;
    --backdrop: #ececec;
    --photo-light: #d9d9d9;
    --photo-dark: #6f6f6f;
  }
  * { box-sizing: border-box; margin: 0; padding: 0; }
  html, body { width: 1200px; height: 900px; overflow: hidden; }
  body {
    background: var(--backdrop);
    display: flex; flex-direction: column; align-items: center; justify-content: center;
    gap: 40px;
    font-family: "Arimo", Arial, sans-serif;
  }
  .card {
    position: relative; width: 700px; height: 400px; overflow: hidden;
    box-shadow: 0 6px 18px rgba(0,0,0,.18);
  }

  /* Brand lockup */
  .brand {
    display: flex; align-items: center; gap: 16px;
    font-family: "Cinzel", serif; font-weight: 400; white-space: nowrap;
  }
  .brand-mark { width: 58px; height: 58px; border: 3px solid currentColor; flex: none; }
  .brand-name { font-size: 30px; letter-spacing: 1px; line-height: 1.1; }
  .brand-name small { display: block; font-size: 14px; letter-spacing: 2px; text-align: right; }

  /* Back */
  .card-back { background: var(--crimson); color: var(--paper); }
  .card-back .brand { position: absolute; left: 50%; top: 120px; transform: translateX(-50%); }
  .broker {
    position: absolute; left: 120px; bottom: 42px;
    display: flex; flex-direction: column; align-items: center; gap: 8px;
    font-family: "Cinzel", serif; font-size: 13px; letter-spacing: 2px;
  }
  .broker-mark { width: 52px; height: 52px; border-radius: 50%; border: 2px solid var(--paper); }
  .badges { position: absolute; right: 90px; bottom: 70px; display: flex; gap: 8px; align-items: center; }
  .badge { border: 2px solid var(--paper); }
  .badge-housing { width: 44px; height: 40px; }
  .badge-realtor { width: 40px; height: 40px; }
  .badge-listing { width: 78px; height: 28px; }

  /* Front */
  .card-front { background: var(--paper); }
  .card-front .brand { position: absolute; left: 36px; top: 40px; color: var(--crimson); gap: 14px; }
  .card-front .brand-mark { width: 52px; height: 52px; }
  .card-front .brand-name { font-size: 24px; }
  .card-front .brand-name small { font-size: 12px; }
  .photo {
    position: absolute; right: 30px; top: 24px; width: 220px; height: 290px;
    background: radial-gradient(ellipse at 50% 35%, var(--photo-light), var(--photo-dark));
  }
  .wave { position: absolute; inset: 0; width: 100%; height: 100%; }
  .contact { position: absolute; left: 48px; top: 180px; }
  .person-name { font-family: "Cinzel", serif; font-weight: 600; font-size: 30px; color: var(--crimson); letter-spacing: 1px; }
  .person-title { font-size: 17px; color: var(--charcoal); letter-spacing: 1px; margin: 2px 0 14px; }
  .contact-line { display: flex; align-items: center; gap: 10px; font-size: 19px; color: var(--ink); margin-bottom: 6px; }
  .contact-line svg { width: 18px; height: 18px; fill: var(--crimson); flex: none; }
  .website { position: absolute; right: 40px; bottom: 36px; color: var(--paper); font-size: 18px; letter-spacing: .5px; }
</style>
</head>
<body>

<section class="card card-back">
  <div class="brand">
    <span class="brand-mark"></span>
    <span class="brand-name">LORENA WHITFIELD<small>REAL ESTATE</small></span>
  </div>
  <div class="broker">
    <span class="broker-mark"></span>
    <span>HARLAN RIDGE REAL ESTATE</span>
  </div>
  <div class="badges">
    <span class="badge badge-housing"></span>
    <span class="badge badge-realtor"></span>
    <span class="badge badge-listing"></span>
  </div>
</section>

<section class="card card-front">
  <div class="photo" role="img" aria-label="Portrait photo of Lorena Whitfield"></div>
  <svg class="wave" viewBox="0 0 700 400" preserveAspectRatio="none">
    <path d="M0,338 C250,332 470,300 700,190 L700,205 C500,300 260,345 0,352 Z" fill="var(--charcoal)"/>
    <path d="M0,358 C260,352 500,305 700,212 L700,400 L0,400 Z" fill="var(--crimson)"/>
  </svg>
  <div class="brand">
    <span class="brand-mark"></span>
    <span class="brand-name">LORENA WHITFIELD<small>REAL ESTATE</small></span>
  </div>
  <div class="contact">
    <h1 class="person-name">LORENA WHITFIELD</h1>
    <p class="person-title">REALTOR</p>
    <p class="contact-line">
      <svg viewBox="0 0 24 24"><path d="M6.6 10.8a15.1 15.1 0 0 0 6.6 6.6l2.2-2.2c.3-.3.7-.4 1-.2 1.1.4 2.3.6 3.6.6.6 0 1 .4 1 1V20c0 .6-.4 1-1 1A17 17 0 0 1 3 4c0-.6.4-1 1-1h3.5c.6 0 1 .4 1 1 0 1.3.2 2.5.6 3.6.1.3 0 .7-.2 1z"/></svg>
      480-555-0137
    </p>
    <p class="contact-line">
      <svg viewBox="0 0 24 24"><path d="M2 5h20v14H2z M4 7v.5l8 5.5 8-5.5V7l-8 5.5z" fill-rule="evenodd"/></svg>
      Lorena@LorenaWhitfieldRE.com
    </p>
  </div>
  <p class="website">www.LorenaWhitfieldRE.com</p>
</section>

</body>
</html>
```